Cat sitting business Web Design Project ***

I have a cat sitting business where I either take care of cats in their home or board them in mine

I need a website which offers my services, my rates, about me, FAQ's, Hours of operation and service areas covered, testimonials, contact info, newsletter sign up, gallery of photos and the ability for me to go in and update when needed.

Coded - Design and coding required

5+ page

```html
<!DOCTYPE html>
<html lang="en">
<head>
<meta charset="utf-8">
<title>Velvet Paw Cat Sitting</title>
<link href="https://fonts.googleapis.com/css2?family=Nunito:wght@700;800;900&family=Montserrat:wght@400;500;600;700&family=Mrs+Saint+Delafield&display=swap" rel="stylesheet">
<style>
:root{
  --rose:#a9585c;
  --rose-dark:#8f4548;
  --green:#8cc44c;
  --green-dark:#76ad37;
  --ink:#3a3a3a;
  --muted:#6b6b6b;
  --paper:#fbf8f6;
  --white:#ffffff;
  --line:#e9e2e2;
}
*{box-sizing:border-box;margin:0;padding:0}
html,body{width:1200px;height:4325px;overflow:hidden}
body{position:relative;background:var(--white);font-family:'Montserrat',sans-serif;color:var(--ink)}
.abs{position:absolute}
.heading{font-family:'Nunito',sans-serif;font-weight:800;color:var(--ink)}
.script{font-family:'Mrs Saint Delafield',cursive;color:var(--rose);font-size:46px;line-height:1}
.body-text{font-size:15px;line-height:18px;color:var(--muted)}
.btn{position:absolute;display:flex;align-items:center;justify-content:center;border-radius:20px;font-size:11px;font-weight:700;color:var(--white);background:var(--green)}
.photo{position:absolute;border-radius:4px}

/* top bar */
.topbar{left:0;top:0;width:1200px;height:30px;background:var(--rose);color:var(--white);font-size:10px;font-weight:500}
.topbar span{position:absolute;top:9px}
.social{position:absolute;display:flex;gap:7px}
.social i{display:block;width:14px;height:14px;border:1.5px solid currentColor;border-radius:50%}

/* nav */
.brand{left:112px;top:46px;width:90px;text-align:center;font-family:'Nunito',sans-serif;font-weight:800;font-size:12px;color:var(--rose);line-height:14px}
.brand b{display:block;width:34px;height:34px;margin:0 auto 4px;border:2px solid var(--green);border-radius:50%}
.nav{top:68px;font-size:11px;font-weight:600;color:var(--ink)}
.nav.active{color:var(--green)}
.nav-cta{left:1027px;top:64px;width:84px;height:22px;background:var(--rose);color:var(--white);font-size:11px;font-weight:700;display:flex;align-items:center;justify-content:center;border-radius:3px;transform:skewX(-8deg)}

/* hero */
.hero-title{left:120px;top:222px;font-size:50px;line-height:60px}
.hero-title .r{color:var(--rose)} .hero-title .g{color:var(--green)}
.btn-outline{background:transparent;color:var(--rose);border:1.5px solid var(--rose)}
.frame{left:610px;top:120px;width:505px;height:548px;background:var(--white);border-radius:30px;box-shadow:0 6px 18px rgba(0,0,0,.12)}

/* services */
.svc-icon{width:100px;height:100px;border-radius:50%;display:flex;align-items:center;justify-content:center}
.svc-icon.rose{background:var(--rose)} .svc-icon.green{background:var(--green)}
.badge{width:28px;height:28px;border-radius:50%;color:var(--white);font-size:11px;font-weight:700;display:flex;align-items:center;justify-content:center;border:3px solid var(--white)}
.svc-title{width:240px;text-align:center;font-size:20px}
.svc-text{width:240px;text-align:center}
.check-row{right:90px;font-size:11px;font-weight:700;color:var(--ink);display:flex;align-items:center;gap:8px}
.tick{width:18px;height:18px;border-radius:50%;background:var(--rose);display:flex;align-items:center;justify-content:center}

/* testimonial */
.quote-mark{font-family:'Nunito',sans-serif;font-weight:900;font-size:130px;line-height:1;color:transparent;-webkit-text-stroke:3px var(--white)}
.arrow-dot{width:32px;height:32px;border-radius:50%;background:var(--rose)}

/* faq */
.acc{left:723px;width:393px;background:#f6f3f3;border-left:3px solid var(--white)}
.acc-head{height:47px;display:flex;align-items:center;justify-content:space-between;padding:0 22px;font-size:15px;font-weight:700;color:var(--rose)}

/* pricing */
.card{top:3025px;width:260px;height:519px;background:var(--white);box-shadow:0 4px 16px rgba(0,0,0,.12)}
.card .photo{left:0;top:0;width:260px;height:138px;border-radius:0}
.price{position:absolute;left:25px;top:158px;width:54px;height:27px;background:var(--green);color:var(--white);font-family:'Nunito',sans-serif;font-weight:800;font-size:19px;display:flex;align-items:center;justify-content:center;border-radius:2px}
.plan{position:absolute;left:101px;top:156px;font-size:22px}
.card .sub{position:absolute;left:34px;top:192px;font-size:24px}
.card .body-text{position:absolute;left:20px;top:239px;width:220px;text-align:center}
.perk{position:absolute;left:38px;display:flex;align-items:center;gap:12px;font-size:14px;font-weight:700;color:var(--ink)}
.perk .tick{width:26px;height:26px;background:var(--green)}

/* footer */
.partner{top:3634px;width:72px;height:14px;background:#d9d3d3;border-radius:7px}
.field{height:44px;border:1.5px solid var(--white);border-radius:24px;color:var(--white);font-size:12px;font-weight:700;display:flex;align-items:center;padding-left:20px}
.foot-title{font-size:14px;font-weight:700;color:var(--white)}
.foot-list{font-size:10px;font-weight:600;color:var(--white);line-height:25px}
</style>
</head>
<body>

<!-- top bar -->
<div class="abs topbar">
  <svg class="abs" style="left:122px;top:9px" width="12" height="12" viewBox="0 0 24 24"><path fill="#fff" d="M6.6 10.8a15 15 0 0 0 6.6 6.6l2.2-2.2c.3-.3.7-.4 1-.2 1.1.4 2.3.6 3.6.6.6 0 1 .4 1 1V20c0 .6-.4 1-1 1A17 17 0 0 1 3 4c0-.6.4-1 1-1h3.5c.6 0 1 .4 1 1 0 1.3.2 2.5.6 3.6.1.3 0 .7-.2 1z"/></svg>
  <span style="left:148px">123-456-789</span>
  <svg class="abs" style="left:255px;top:9px" width="13" height="11" viewBox="0 0 24 18"><rect x="1" y="1" width="22" height="16" fill="none" stroke="#fff" stroke-width="2"/><path d="M1 1l11 9 11-9" fill="none" stroke="#fff" stroke-width="2"/></svg>
  <span style="left:282px">Info@youremail.com</span>
  <svg class="abs" style="left:423px;top:9px" width="12" height="12" viewBox="0 0 24 24"><circle cx="12" cy="12" r="10" fill="none" stroke="#fff" stroke-width="2"/><path d="M12 6v6l4 2" fill="none" stroke="#fff" stroke-width="2"/></svg>
  <span style="left:451px">Your Email Here</span>
  <div class="social" style="left:982px;top:8px;color:#fff"><i></i><i></i><i></i><i></i><i></i><i></i></div>
</div>

<!-- hero background -->
<svg class="abs" style="left:0;top:30px" width="1200" height="560"><path d="M0 0H1200V470C1050 520 900 560 700 540 500 520 250 500 0 520Z" fill="var(--paper)"/></svg>

<!-- nav -->
<div class="abs brand"><b></b>Velvet Paw<br>Cat Sitting</div>
<div class="abs nav active" style="left:535px">Home</div>
<div class="abs nav" style="left:616px">About</div>
<div class="abs nav" style="left:697px">Services</div>
<div class="abs nav" style="left:790px">Pricings</div>
<div class="abs nav" style="left:883px">FAQs</div>
<div class="abs nav" style="left:960px">Blogs</div>
<div class="abs nav-cta"><span style="transform:skewX(8deg)">Contact Me</span></div>

<!-- hero -->
<h1 class="abs heading hero-title"><span class="r">Devoted to Proper</span><br><span class="g">Cat Sitting</span><br><span class="r">Services</span></h1>
<div class="btn" style="left:119px;top:433px;width:114px;height:30px">View Services</div>
<div class="btn btn-outline" style="left:257px;top:433px;width:99px;height:30px">Contact Me</div>

<div class="abs frame"></div>
<div class="photo" role="img" aria-label="Cat being stroked under the chin" style="left:621px;top:131px;width:226px;height:213px;background:linear-gradient(135deg,#8a7a6e,#cdb9a8)"></div>
<div class="photo" role="img" aria-label="Cat napping on a knitted blanket" style="left:874px;top:131px;width:228px;height:292px;background:linear-gradient(160deg,#5b3a2c,#e9e3dc 60%)"></div>
<div class="photo" role="img" aria-label="Orange cat sleeping" style="left:621px;top:361px;width:226px;height:290px;background:linear-gradient(135deg,#d9a272,#b56a35)"></div>
<div class="photo" role="img" aria-label="Woman petting a fluffy cat" style="left:874px;top:450px;width:228px;height:204px;background:linear-gradient(135deg,#c47c52,#eee6e0)"></div>

<!-- services -->
<div class="abs svc-icon rose" style="left:190px;top:844px"><svg width="44" height="44" viewBox="0 0 24 24" fill="none" stroke="#fff" stroke-width="1.4"><rect x="3" y="6" width="18" height="13" rx="2"/><path d="M7 6l2-3M17 6l-2-3M9 12h.01M15 12h.01"/></svg></div>
<div class="abs badge" style="left:275px;top:824px;background:var(--rose)">1</div>
<div class="abs svc-icon green" style="left:458px;top:844px"><svg width="44" height="44" viewBox="0 0 24 24" fill="none" stroke="#fff" stroke-width="1.4"><path d="M6 20c0-6 3-9 6-9s6 3 6 9zM9 8l1-4 2 2 2-2 1 4"/></svg></div>
<div class="abs badge" style="left:543px;top:824px;background:var(--green)">2</div>
<div class="abs svc-icon green" style="left:190px;top:1079px"><svg width="44" height="44" viewBox="0 0 24 24" fill="none" stroke="#fff" stroke-width="1.4"><circle cx="12" cy="15" r="5"/><path d="M12 13v4M10 15h4"/><circle cx="6" cy="9" r="1.6"/><circle cx="10" cy="5" r="1.6"/><circle cx="14" cy="5" r="1.6"/><circle cx="18" cy="9" r="1.6"/></svg></div>
<div class="abs badge" style="left:275px;top:1063px;background:var(--green)">3</div>
<div class="abs svc-icon rose" style="left:458px;top:1079px"><svg width="44" height="44" viewBox="0 0 24 24" fill="none" stroke="#fff" stroke-width="1.4"><path d="M3 11l9-7 9 7M5 10v10h14V10"/><path d="M9 20v-5h6v5"/></svg></div>
<div class="abs badge" style="left:543px;top:1063px;background:var(--rose)">4</div>

<div class="abs heading svc-title" style="left:120px;top:958px">Cat Sitting</div>
<div class="abs body-text svc-text" style="left:120px;top:993px">Lorem Ipsum is simply<br>dummy text of the printing<br>and typesetting industry.</div>
<div class="abs heading svc-title" style="left:388px;top:958px">Cat Training</div>
<div class="abs body-text svc-text" style="left:388px;top:993px">Lorem Ipsum is simply<br>dummy text of the printing<br>and typesetting industry.</div>
<div class="abs heading svc-title" style="left:120px;top:1193px">Full Diagnostics</div>
<div class="abs body-text svc-text" style="left:120px;top:1228px">Lorem Ipsum is simply<br>dummy text of the printing<br>and typesetting industry.</div>
<div class="abs heading svc-title" style="left:388px;top:1193px">Cat Breeding</div>
<div class="abs body-text svc-text" style="left:388px;top:1228px">Lorem Ipsum is simply<br>dummy text of the printing<br>and typesetting industry.</div>

<div class="abs script" style="right:85px;top:845px">What we do?</div>
<h2 class="abs heading" style="right:83px;top:910px;font-size:36px;line-height:44px;text-align:right">How we help you<br>professionaly?</h2>
<p class="abs body-text" style="right:90px;top:1025px;width:360px;text-align:right;font-size:13px;line-height:17px">Lorem Ipsum is simply dummy text of the print-ing and typesetting industry. Lorem Ipsum has been the industry's standard dummy text ever</p>
<div class="abs check-row" style="top:1098px">That as guard as fresh lady careful a they he l sitting. <span class="tick"><svg width="10" height="10" viewBox="0 0 10 10"><path d="M2 5l2 2 4-4" stroke="#fff" stroke-width="1.6" fill="none"/></svg></span></div>
<div class="abs check-row" style="top:1128px">That as guard as fresh lady careful a they he l sitting. <span class="tick"><svg width="10" height="10" viewBox="0 0 10 10"><path d="M2 5l2 2 4-4" stroke="#fff" stroke-width="1.6" fill="none"/></svg></span></div>
<div class="abs check-row" style="top:1158px">That as guard as fresh lady careful a they he l sitting. <span class="tick"><svg width="10" height="10" viewBox="0 0 10 10"><path d="M2 5l2 2 4-4" stroke="#fff" stroke-width="1.6" fill="none"/></svg></span></div>
<div class="btn" style="left:995px;top:1198px;width:116px;height:32px">Discover More</div>

<!-- about -->
<div class="photo" role="img" aria-label="Cat sitter holding a white cat on a sofa" style="left:619px;top:1426px;width:581px;height:520px;border-radius:0;background:linear-gradient(135deg,#7a6e62,#c9a57a 55%,#e8dfd6)"></div>
<div class="abs script" style="left:122px;top:1505px">About us</div>
<h2 class="abs heading" style="left:120px;top:1562px;font-size:34px">How did we get <span style="background:var(--green);color:#fff;padding:0 4px">here?</span></h2>
<p class="abs body-text" style="left:122px;top:1622px;width:430px;font-size:14.5px;line-height:18px">Lorem Ipsum is simply dummy text of the printing and typesetting industry. Lorem Ipsum has been the industry's standard dummy text ever since the 1500s, when an unknown printer took a galley of type and scrambled it to make a type specimen book. It has survived not only five centuries, but also the leap into electronic typesetting, remaining essentially unchanged. It was popularised in the 1960s with the release of Letraset sheets con-</p>
<div class="btn" style="left:122px;top:1805px;width:118px;height:32px">Contact Me</div>

<!-- testimonial -->
<svg class="abs" style="left:0;top:1946px" width="1200" height="310"><path d="M0 0H1200V250C1120 220 1060 220 990 245 900 280 820 285 740 250 660 215 580 215 500 250 420 285 340 280 260 245 180 215 100 215 0 250Z" fill="var(--green)"/></svg>
<div class="abs quote-mark" style="left:248px;top:1960px">“</div>
<div class="abs quote-mark" style="left:872px;top:2075px">”</div>
<h2 class="abs heading" style="left:0;width:1200px;top:1968px;text-align:center;font-size:36px;color:#fff">They’ve said about us</h2>
<p class="abs" style="left:250px;top:2040px;width:700px;text-align:center;font-size:14px;line-height:18px;color:#fff">Lorem Ipsum is simply dummy text of the printing and typesetting industry. Lorem Ipsum has been the industry's standard dummy text ever since the 1500s, when an unknown printer took a galley of type Lorem Ipsum is simply dummy text of the printing and typesetting indus-</p>
<div class="abs" role="img" aria-label="Portrait of the reviewer" style="left:435px;top:2113px;width:70px;height:70px;border-radius:50%;border:3px solid #fff;background:linear-gradient(135deg,#c9a06a,#6b4c39)"></div>
<div class="abs heading" style="left:513px;top:2108px;font-size:26px;color:#fff">Maren Holt</div>
<div class="abs script" style="left:540px;top:2140px;font-size:22px;color:#fff">Business Owner Ltd</div>
<div class="abs" style="left:553px;top:2170px;font-size:16px;letter-spacing:6px;color:#f6c343">★★★★★</div>
<div class="abs arrow-dot" style="left:60px;top:2080px"></div>
<svg class="abs" style="left:62px;top:2086px" width="70" height="20"><path d="M6 10c20-6 40-6 60 2M6 10l6-5M6 10l5 5" stroke="#fff" stroke-width="1.5" fill="none"/></svg>
<div class="abs arrow-dot" style="left:1107px;top:2080px"></div>
<svg class="abs" style="left:1070px;top:2086px" width="70" height="20"><path d="M4 12c20-8 40-8 60-2M64 10l-6-5M64 10l-5 5" stroke="#fff" stroke-width="1.5" fill="none"/></svg>

<!-- faq -->
<div class="abs script" style="left:132px;top:2335px;font-size:40px">Frequently asked questions</div>
<h2 class="abs heading" style="left:120px;top:2402px;font-size:34px;line-height:44px">We are working for the<br><span style="background:var(--green);color:#fff;padding:0 6px 0 4px">community</span></h2>
<p class="abs body-text" style="left:118px;top:2525px;width:430px;font-size:14.5px;line-height:18px">Lorem Ipsum is simply dummy text of the printing and typesetting industry. Lorem Ipsum has been the industry's standard dummy text ever since the 1500s, when an unknown printer took a galley of type and scrambled it to make a type specimen book. It has survived not only five centuries, but also the leap into electronic typeset-</p>
<div class="abs" style="left:120px;top:2667px;width:42px;height:42px;border-radius:50%;background:var(--rose);display:flex;align-items:center;justify-content:center"><svg width="20" height="20" viewBox="0 0 24 24"><path fill="#fff" d="M6.6 10.8a15 15 0 0 0 6.6 6.6l2.2-2.2c.3-.3.7-.4 1-.2 1.1.4 2.3.6 3.6.6.6 0 1 .4 1 1V20c0 .6-.4 1-1 1A17 17 0 0 1 3 4c0-.6.4-1 1-1h3.5c.6 0 1 .4 1 1 0 1.3.2 2.5.6 3.6.1.3 0 .7-.2 1z"/></svg></div>
<div class="abs heading" style="left:178px;top:2670px;font-size:26px">123-456-789</div>

<div class="abs acc" style="top:2327px;height:161px">
  <div class="acc-head" style="border-bottom:1px solid var(--line)">What is cat sitting <span>˄</span></div>
  <p class="body-text" style="padding:10px 22px;font-size:14px;line-height:17px">Lorem Ipsum is simply dummy text of the printing and typesetting industry. Lorem Ipsum has been the industry's standard dummy text ever since the 1500s, when an unknown printer took</p>
</div>
<div class="abs acc" style="top:2512px"><div class="acc-head">What is cat sitting <span>˅</span></div></div>
<div class="abs acc" style="top:2579px"><div class="acc-head">What is cat sitting <span>˅</span></div></div>
<div class="abs acc" style="top:2646px"><div class="acc-head">What is cat sitting <span>˅</span></div></div>

<!-- pricing -->
<div class="abs script" style="left:0;width:1200px;text-align:center;top:2868px">Bring your pets</div>
<h2 class="abs heading" style="left:0;width:1200px;text-align:center;top:2930px;font-size:36px">The Best Choice</h2>

<div class="abs card" style="left:193px">
  <div class="photo" role="img" aria-label="Long-haired cat lying on a sofa" style="background:linear-gradient(135deg,#d9cbb8,#6e6256)"></div>
  <div class="price">90$</div><div class="heading plan">Basic Plan</div><div class="script sub">Per Visit</div>
  <p class="body-text">Lorem Ipsum is simply dummy text of the printing and typesetting industry. Lorem Ipsum has been the industry's standard dummy text ever since the 1500s,</p>
  <div class="perk" style="top:3384px"><span class="tick"><svg width="12" height="12" viewBox="0 0 10 10"><path d="M2 5l2 2 4-4" stroke="#fff" stroke-width="1.6" fill="none"/></svg></span>Dui sapien eget mi.</div>
</div>
<div class="abs card" style="left:470px">
  <div class="photo" role="img" aria-label="Woman cuddling a tabby cat" style="background:linear-gradient(135deg,#efe7dc,#c49a6a)"></div>
  <div class="price">90$</div><div class="heading plan">Great Plan</div><div class="script sub">Per Visit</div>
  <p class="body-text">Lorem Ipsum is simply dummy text of the printing and typesetting industry. Lorem Ipsum has been the industry's standard dummy text ever since the 1500s,</p>
</div>
<div class="abs card" style="left:747px">
  <div class="photo" role="img" aria-label="Tabby cat beside a scratching pad" style="background:linear-gradient(135deg,#8c7a68,#d8d2cc)"></div>
  <div class="price">90$</div><div class="heading plan">Big Plan</div><div class="script sub">Per Visit</div>
  <p class="body-text">Lorem Ipsum is simply dummy text of the printing and typesetting industry. Lorem Ipsum has been the industry's standard dummy text ever since the 1500s,</p>
</div>
<!-- perks -->
<div class="abs" style="left:193px;top:3383px;width:814px;height:140px">
  <div class="perk" style="left:38px;top:0"><span class="tick"><svg width="12" height="12" viewBox="0 0 10 10"><path d="M2 5l2 2 4-4" stroke="#fff" stroke-width="1.6" fill="none"/></svg></span>Dui sapien eget mi.</div>
  <div class="perk" style="left:38px;top:49px"><span class="tick"><svg width="12" height="12" viewBox="0 0 10 10"><path d="M2 5l2 2 4-4" stroke="#fff" stroke-width="1.6" fill="none"/></svg></span>Dui sapien eget mi.</div>
  <div class="perk" style="left:38px;top:98px"><span class="tick"><svg width="12" height="12" viewBox="0 0 10 10"><path d="M2 5l2 2 4-4" stroke="#fff" stroke-width="1.6" fill="none"/></svg></span>Dui sapien eget mi.</div>
  <div class="perk" style="left:315px;top:0"><span class="tick"><svg width="12" height="12" viewBox="0 0 10 10"><path d="M2 5l2 2 4-4" stroke="#fff" stroke-width="1.6" fill="none"/></svg></span>Dui sapien eget mi.</div>
  <div class="perk" style="left:315px;top:49px"><span class="tick"><svg width="12" height="12" viewBox="0 0 10 10"><path d="M2 5l2 2 4-4" stroke="#fff" stroke-width="1.6" fill="none"/></svg></span>Dui sapien eget mi.</div>
  <div class="perk" style="left:315px;top:98px"><span class="tick"><svg width="12" height="12" viewBox="0 0 10 10"><path d="M2 5l2 2 4-4" stroke="#fff" stroke-width="1.6" fill="none"/></svg></span>Dui sapien eget mi.</div>
  <div class="perk" style="left:592px;top:0"><span class="tick"><svg width="12" height="12" viewBox="0 0 10 10"><path d="M2 5l2 2 4-4" stroke="#fff" stroke-width="1.6" fill="none"/></svg></span>Dui sapien eget mi.</div>
  <div class="perk" style="left:592px;top:49px"><span class="tick"><svg width="12" height="12" viewBox="0 0 10 10"><path d="M2 5l2 2 4-4" stroke="#fff" stroke-width="1.6" fill="none"/></svg></span>Dui sapien eget mi.</div>
  <div class="perk" style="left:592px;top:98px"><span class="tick"><svg width="12" height="12" viewBox="0 0 10 10"><path d="M2 5l2 2 4-4" stroke="#fff" stroke-width="1.6" fill="none"/></svg></span>Dui sapien eget mi.</div>
</div>

<!-- footer area -->
<svg class="abs" style="left:0;top:3560px" width="1200" height="765"><path d="M0 0C60 80 140 160 300 190 520 230 800 200 1000 205 1100 208 1160 215 1200 225V765H0Z" fill="var(--rose)"/></svg>
<div class="abs partner" style="left:196px"></div>
<div class="abs partner" style="left:342px"></div>
<div class="abs partner" style="left:493px"></div>
<div class="abs partner" style="left:637px"></div>
<div class="abs partner" style="left:783px"></div>
<div class="abs partner" style="left:929px"></div>

<h2 class="abs heading" style="left:0;width:1150px;text-align:center;top:3860px;font-size:34px;color:#fff">Get New Insight Weekly</h2>
<p class="abs" style="left:350px;top:3912px;width:450px;text-align:center;font-size:14px;line-height:17px;color:#fff">Lorem Ipsum is simply dummy text of the printing and typesetting industry. Lorem Ipsum has been the indus-</p>
<div class="abs field" style="left:270px;top:3977px;width:262px">NAME</div>
<div class="abs field" style="left:557px;top:3977px;width:332px">EMAIL</div>
<div class="btn" style="left:774px;top:3981px;width:110px;height:36px;font-size:12px">SUBSCRIBE</div>

<div class="abs" style="left:270px;top:4061px;width:94px;height:101px;background:#fff;border-radius:0 0 47px 47px;display:flex;flex-direction:column;align-items:center;justify-content:center;font-family:'Nunito',sans-serif;font-weight:800;font-size:10px;line-height:12px;color:var(--rose);text-align:center"><b style="display:block;width:28px;height:28px;border:2px solid var(--green);border-radius:50%;margin-bottom:4px"></b>Velvet Paw<br>Cat Sitting</div>
<p class="abs" style="left:266px;top:4180px;width:190px;font-size:13px;line-height:16px;color:#fff">Lorem Ipsum is simply dummy text of the printing and typesetting industry.</p>
<div class="social" style="left:268px;top:4247px;color:#fff"><i></i><i></i><i></i><i></i><i></i><i></i></div>

<div class="abs foot-title" style="left:525px;top:4062px">Quick Links</div>
<div class="abs foot-list" style="left:525px;top:4091px">Home<br>About<br>Services<br>Pricings<br>FAQs<br>Blogs</div>
<div class="abs foot-title" style="left:675px;top:4062px">Contact Me</div>
<div class="abs foot-list" style="left:703px;top:4091px">123-456-789<br>Your Address Here<br>Your Email Here<br>Your Web Here</div>
<svg class="abs" style="left:674px;top:4096px" width="14" height="92" viewBox="0 0 14 92" fill="none" stroke="#fff" stroke-width="1.3"><path d="M3 2c1 4 4 7 8 8l1-2"/><path d="M1 32l6-5 6 5M3 31v6h8v-6"/><rect x="1" y="53" width="12" height="8"/><path d="M1 53l6 4 6-4"/><circle cx="7" cy="82" r="6"/><path d="M1 82h12M7 76c-3 4-3 8 0 12M7 76c3 4 3 8 0 12"/></svg>
<div class="abs foot-title" style="left:859px;top:4062px">Working Hours</div>
<p class="abs" style="left:862px;top:4087px;width:130px;font-size:11px;line-height:13px;color:#fff">Our support available to help you 24 hours a day. We provide our best.</p>
<div class="abs foot-list" style="left:862px;top:4142px;font-size:9.5px">Mon - Fri : 08.00 am - 20.00 pm<br>Saturday : 09.00 am - 20.00 pm<br>Sunday : We Are Closed</div>

<div class="abs" style="left:0;top:4293px;width:1200px;height:32px;background:var(--green);color:#fff;font-size:13px;font-weight:700;display:flex;align-items:center;justify-content:center">copyright: all right reserved to velvetpawcatsitting.com, 2022</div>

</body>
</html>
```